CBD Boutique Business Card Needed

We are in need of a business card to reflect the direction of our latest products. We are a fully organic company in which our store and products are very heavy in wood and "natural" components. We decided to bring color into one of our brands and immediately knew this is where we needed to go.

We are NOT a cash grab CBD company. We could have done this wrong, slapped a label on a shit product and left it like that. I am passionate about sharing my experience with other veterans and opening a store and making it a comfortable place for others to come and see if they can have the same experience.

Target Market(s)

We are a dual market company. We do have a beauty line that will cover the costs of the majority of our business. But we also heavily cater to veterans and first responders. I am a veteran and this is how I found out about CBD. So the marketing needs to bring in our higher end beauty clientele but also be able to not put off our customers that readily need this.

Contact Information for Business Card

What we are looking for is a light, professional, boutique design that is is neither quite feminine or masculine. Attached is a picture of a store in Portland that we asked our store designer to get her inspiration from. But all natural wood and black outlines are what is mostly in there.

Attached are the following files:

Logo: An AI file with how we have our logo. I do not understand AI and have no idea why the letters are individual. The font is Adam. OLU is the logo and Tonics of Vigor is our tagline.

KM Vantage (front and back) cards I did originally found at a trade show that I absolutely loved...while it is mostly there and I would still be happy with them but it is me pretending to be you. I understand I am not and there is probably a lot wrong that all of you would see instantly and this is why I am here.

Dropper Bottle: This is our final product mock up

Water Color: I am semi flexible here. This water color is slightly different on every level of our brand. The color itself can change...we are not stuck on THIS particular one. If you happen to make a new one that is similar in style and we use it...then I will happily commission you to change the rest on our next product run. I am pretty sure you can use this statement as evidence later . =) .

But seriously, we heavily believe in pay it forward and will work with anyone here that may have a vision bigger than ours. The winner of this contest will get preferential consideration on our marketing materials (need letterhead etc. next, as well as a brochure, and website) so three more projects coming down the pipeline.

Information to use for your mockup is contained on the card images I have included. I would prefer ROOTED IN CALM GROWN FOR YOU to be more prominent. No where else on the card do we have CBD mentioned.

Font styles to use
Sans Serif

Colors

Designer to choose colors to be used in the design.

Requirements
Must have
• Double Sided
• Front: OLU logo on front of card will be raised embossed. Background is watercolor. One has been provided. Others are up for consideration. If the rest of your design is incredible and I don't like your watercolor I will just ask to swap it.
• Back: Standard information. Not stuck on anything here. I LOVE clean minimal designs. The bleed on the card I provided is a luxury...
• Font for title and OLU is Adam. Everything else I prefer san serif or as clean as possible.
Nice to have
• I Need to incorporate Naturally Nurturing somewhere on the card. Bold but not intrusive.

```html
<!DOCTYPE html>
<html lang="en">
<head>
<meta charset="UTF-8">
<title>OLU – Business Card</title>
<link href="https://fonts.googleapis.com/css2?family=Montserrat:wght@300;400;700&family=Lato:wght@400&display=swap" rel="stylesheet">
<style>
  :root {
    --backdrop: #e9e7e4;
    --card: #ffffff;
    --ink: #111111;
    --rule: #222222;
    --wash-orange: #e3924a;
    --wash-rust: #c8732c;
    --wash-peach: #f0c38e;
    --wash-teal: #4fb3c2;
    --wash-deep-teal: #1f8d9a;
    --wash-mist: #d7eef0;
  }
  * { margin: 0; padding: 0; box-sizing: border-box; }
  html, body { width: 1200px; height: 1200px; overflow: hidden; }
  body { background: var(--backdrop); position: relative; font-family: "Lato", sans-serif; color: var(--ink); }

  .card {
    position: absolute;
    top: 310px;
    height: 594px;
    background: var(--card);
    overflow: hidden;
  }
  .card--back { left: 234px; width: 364px; }
  .card--front { left: 627px; width: 369px; }

  .wordmark {
    position: absolute;
    left: 0; right: 0;
    text-align: center;
    font-family: "Montserrat", sans-serif;
    font-weight: 300;
    color: var(--ink);
  }
  .wordmark__name { display: block; font-size: 104px; letter-spacing: 10px; line-height: 1; }
  .wordmark__tagline { display: block; font-size: 21px; letter-spacing: 2px; text-transform: uppercase; margin-top: 6px; }
  .card--back .wordmark { top: 90px; }
  .card--front .wordmark { top: 226px; }

  .holder { position: absolute; top: 314px; left: 0; right: 0; text-align: center; font-family: "Montserrat", sans-serif; }
  .holder__name { font-weight: 700; font-size: 21px; letter-spacing: 0.5px; }
  .holder__title { font-weight: 400; font-size: 16px; margin-top: 0; }

  .contact-divider { position: absolute; top: 374px; left: 87px; width: 190px; height: 26px; }

  .contact-list { position: absolute; top: 410px; left: 0; right: 0; text-align: center; font-size: 16.5px; line-height: 22px; }

  .address-rule { position: absolute; top: 485px; left: 88px; width: 195px; height: 1px; background: var(--rule); }
  .address { position: absolute; top: 496px; left: 0; right: 0; text-align: center; font-size: 16.5px; line-height: 22px; }

  .watercolor {
    position: absolute; inset: 0;
    background:
      radial-gradient(ellipse 55% 35% at 60% 18%, var(--wash-rust) 0%, transparent 70%),
      radial-gradient(ellipse 70% 40% at 50% 35%, var(--wash-orange) 0%, transparent 75%),
      radial-gradient(ellipse 60% 30% at 80% 55%, var(--wash-peach) 0%, transparent 70%),
      radial-gradient(ellipse 55% 30% at 25% 70%, var(--wash-teal) 0%, transparent 75%),
      radial-gradient(ellipse 30% 25% at 55% 88%, var(--wash-deep-teal) 0%, transparent 70%),
      linear-gradient(180deg, var(--wash-peach) 0%, var(--wash-orange) 35%, var(--wash-peach) 55%, var(--wash-teal) 75%, var(--wash-mist) 100%);
  }
  .slogan {
    position: absolute; top: 537px; left: 0; right: 0; text-align: center;
    font-family: "Montserrat", sans-serif; font-weight: 700; font-size: 16px; letter-spacing: -0.2px;
  }
</style>
</head>
<body>

  <section class="card card--back" aria-label="Card back">
    <div class="wordmark">
      <span class="wordmark__name">OLU</span>
      <span class="wordmark__tagline">Tonics of Vigor</span>
    </div>

    <div class="holder">
      <p class="holder__name">DANA WHITFIELD</p>
      <p class="holder__title">OWNER/CEO</p>
    </div>

    <svg class="contact-divider" viewBox="0 0 190 26" aria-hidden="true">
      <line x1="0" y1="13" x2="52" y2="13" stroke="#222" stroke-width="1"/>
      <line x1="138" y1="13" x2="190" y2="13" stroke="#222" stroke-width="1"/>
      <circle cx="68" cy="13" r="12" fill="#111"/>
      <circle cx="95" cy="13" r="12" fill="#111"/>
      <circle cx="122" cy="13" r="12" fill="#111"/>
      <path d="M62 10 q6 -5 12 0 l-2 2 h-8 z M63 12 h10 v5 h-10 z" fill="#fff"/>
      <rect x="89" y="9" width="12" height="8" fill="none" stroke="#fff" stroke-width="1.3"/>
      <path d="M89 9 l6 5 l6 -5" fill="none" stroke="#fff" stroke-width="1.3"/>
      <circle cx="122" cy="13" r="6" fill="none" stroke="#fff" stroke-width="1.3"/>
      <path d="M116 13 h12 M122 7 q-4 6 0 12 q4 -6 0 -12" fill="none" stroke="#fff" stroke-width="1"/>
    </svg>

    <div class="contact-list">
      <p>480.555.0142</p>
      <p>hello@olu.life</p>
      <p>www.olu.life</p>
    </div>

    <div class="address-rule"></div>
    <div class="address">
      <p>2140 N Cedar Ridge Ave</p>
      <p>Mesa, AZ 85201</p>
      <p>Suite 100</p>
    </div>
  </section>

  <section class="card card--front" aria-label="Card front">
    <div class="watercolor" role="img" aria-label="Watercolor wash in burnt orange fading into teal"></div>
    <div class="wordmark">
      <span class="wordmark__name">OLU</span>
      <span class="wordmark__tagline">Tonics of Vigor</span>
    </div>
    <p class="slogan">ROOTED IN CALM GROWN FOR YOU</p>
  </section>

</body>
</html>
```